Lead Generation Postcard Design for Digital Agency Targeting Eye Care Practices

We are a digital marketing agency looking to build our business by offering digital marketing services to a niche market - eye doctors, optometrists. We want to offer them our services and offer a free phone consulting session. They can either call us or visit our web site contact us form (http://www.brightkitemedia.com/contact-us/)We would like to have a design that matches our web site colors, theme, look and feel. But we also want to communicate the eye care industry and somehow the idea of 'digital marketing'.The goal is to get the company to call or contact us for further information.We have saved an example postcard in our account that you can take a look at.

Target Market(s)

eye doctors, optometry practices

Industry/Entity Type

Digital

Other font styles liked:
• see web site for examples

Requirements
Must have
• Big 'gotcha' image.
• matches the look and feel of our web site (www.brightkitemedia.com).
• will send logo when our designer provides... asap.
Should not have
• cheesy looking stock images.

```html
<!DOCTYPE html>
<html lang="en">
<head>
<meta charset="utf-8">
<title>Bright Kite – Eye Care Digital Marketing Postcard</title>
<link href="https://fonts.googleapis.com/css2?family=Archivo+Narrow:ital,wght@1,700&family=Oswald:wght@700&family=Open+Sans:wght@400;700&family=Kalam:wght@700&display=swap" rel="stylesheet">
<style>
  :root {
    --teal: #3a9fb4;
    --teal-dark: #2f8798;
    --red: #d6322b;
    --ink: #1f2a30;
    --text: #5a6268;
    --mist: #eef1f2;
    --white: #ffffff;
    --grey-box: #c9cccd;
  }
  * { margin: 0; padding: 0; box-sizing: border-box; }
  html, body { width: 773px; height: 1200px; overflow: hidden; background: var(--white); }
  .card { position: relative; width: 773px; height: 1200px; font-family: "Open Sans", sans-serif; color: var(--text); }

  /* Front */
  .front { position: absolute; left: 0; top: 0; width: 773px; height: 575px; background: var(--mist); overflow: hidden; }
  .front-pattern { position: absolute; inset: 0 0 40px 0; background: linear-gradient(180deg, #e6eaec, #f3f5f6); }
  .headline-arc { position: absolute; left: 180px; top: 20px; width: 580px; height: 170px; }
  .hero-figure { position: absolute; left: 30px; top: 60px; width: 150px; height: 420px; background: linear-gradient(180deg, #d9dde0, #c5cbcf); border-radius: 70px 70px 10px 10px; }
  .promise { position: absolute; left: 240px; top: 192px; width: 440px; height: 210px; }
  .glasses { position: absolute; left: 540px; top: 370px; width: 180px; height: 95px; background: linear-gradient(135deg, #d0d4d7, #b7bdc1); border-radius: 40px; }
  .brand { position: absolute; display: flex; align-items: center; gap: 6px; font-family: "Oswald", sans-serif; font-weight: 700; color: var(--ink); line-height: 1; }
  .brand-dot { width: 14px; height: 14px; border-radius: 50%; background: var(--red); flex: none; }
  .front .brand { left: 28px; top: 496px; font-size: 26px; }
  .front-band { position: absolute; left: 0; bottom: 0; width: 100%; height: 40px; background: var(--teal); color: var(--white); font-size: 13px; letter-spacing: 2px; display: flex; align-items: center; justify-content: flex-end; padding-right: 60px; }

  /* Back */
  .back { position: absolute; left: 0; top: 575px; width: 773px; height: 625px; }
  .back-title { position: absolute; left: 25px; top: 28px; font-family: "Archivo Narrow", sans-serif; font-style: italic; font-weight: 700; font-size: 32px; color: var(--teal); letter-spacing: 0.5px; }
  .back .brand { left: 535px; top: 112px; font-size: 24px; }
  .brand-stack { display: block; }
  .stamp-box { position: absolute; left: 632px; top: 82px; width: 115px; height: 140px; background: var(--grey-box); }
  .intro { position: absolute; left: 25px; top: 78px; width: 490px; font-size: 15.5px; line-height: 1.5; }
  .intro strong { color: var(--ink); }
  .intro p + p { margin-top: 14px; }
  .rule { position: absolute; left: 25px; top: 318px; width: 722px; border-top: 2px dotted #c4c9cc; }
  .cta-figure { position: absolute; left: 25px; top: 335px; width: 190px; height: 190px; background: linear-gradient(180deg, #e2e5e7, #cdd2d5); border-radius: 12px; }
  .cta-sign { position: absolute; left: 70px; top: 350px; transform: rotate(-12deg); font-family: "Kalam", sans-serif; font-weight: 700; color: var(--red); font-size: 26px; line-height: 1; text-align: center; }
  .offer { position: absolute; left: 240px; top: 405px; width: 300px; font-size: 14px; line-height: 1.5; }
  .back-band { position: absolute; left: 0; bottom: 0; width: 100%; height: 88px; background: var(--teal); color: var(--white); }
  .phone { position: absolute; left: 25px; top: 12px; font-size: 34px; font-weight: 400; letter-spacing: 1px; }
  .contact-url { position: absolute; left: 25px; top: 58px; font-size: 14px; font-weight: 700; }
  .practice { position: absolute; left: 525px; top: 20px; font-size: 11.5px; line-height: 1.4; white-space: nowrap; }
  .practice strong { font-size: 14px; }
</style>
</head>
<body>
<div class="card">
  <section class="front">
    <div class="front-pattern" role="img" aria-label="Soft background of faint cloud and social network icons"></div>
    <svg class="headline-arc" viewBox="0 0 580 170" aria-label="Grow your eye care practice with">
      <defs>
        <path id="arcTop" d="M60 100 Q290 -20 520 100"/>
        <path id="arcLow" d="M150 150 Q290 95 430 150"/>
      </defs>
      <text font-family="Archivo Narrow, sans-serif" font-style="italic" font-weight="700" font-size="38" fill="#3a9fb4"><textPath href="#arcTop" startOffset="50%" text-anchor="middle">GROW YOUR EYE CARE</textPath></text>
      <text font-family="Archivo Narrow, sans-serif" font-style="italic" font-weight="700" font-size="38" fill="#3a9fb4"><textPath href="#arcLow" startOffset="50%" text-anchor="middle">PRACTICE WITH</textPath></text>
    </svg>
    <div class="hero-figure" role="img" aria-label="Cartoon businessman pointing at the headline"></div>
    <svg class="promise" viewBox="0 0 440 210" aria-label="Digital marketing">
      <ellipse cx="220" cy="108" rx="205" ry="88" fill="none" stroke="#d6322b" stroke-width="9" transform="rotate(-4 220 108)"/>
      <text x="220" y="95" text-anchor="middle" font-family="Oswald, sans-serif" font-weight="700" font-size="64" fill="#1f2a30">DIGITAL</text>
      <text x="220" y="162" text-anchor="middle" font-family="Oswald, sans-serif" font-weight="700" font-size="64" fill="#1f2a30">MARKETING</text>
    </svg>
    <div class="glasses" role="img" aria-label="Sketch of eyeglasses"></div>
    <div class="brand"><span class="brand-dot"></span>Bright Kite</div>
    <div class="front-band">www.brightkitemedia.com</div>
  </section>

  <section class="back">
    <h2 class="back-title">BUILD YOUR EYE CARE PRACTICE</h2>
    <div class="stamp-box"></div>
    <div class="brand"><span class="brand-dot"></span><span class="brand-stack">Bright<br>Kite</span></div>
    <div class="intro">
      <p><strong>Are you struggling to grow your optometry practice? Do you have enough high quality Searchly and Rateline reviews? Are you connecting with your Friendbook and Chirper audience? Or maybe you just can't figure out how to use Searchly Ads to bring in more appointment requests?</strong></p>
      <p>We can help. Our agency has worked with other eye care providers and we know the ins and outs of your practice management systems, your patient communication flows and how that all works with digital marketing to grow your business exponentially.</p>
    </div>
    <div class="rule"></div>
    <div class="cta-figure" role="img" aria-label="Cartoon man holding a sign"></div>
    <div class="cta-sign">HURRY!<br>GET STARTED NOW</div>
    <p class="offer">Contact us today and we will send you a free case study of how we helped an eye care provider double their traffic and appointment requests in under a year.</p>
    <div class="back-band">
      <div class="phone">C: 816 555 0142</div>
      <div class="contact-url">http://www.brightkitemedia.com/contact-us/</div>
      <div class="practice"><strong>Dr. Alan Reyes, O.D.</strong><br>Reyes Family Optometry<br>450 Elm Ave, Suite 200, Tulsa, OK 74100</div>
    </div>
  </section>
</div>
</body>
</html>
```